Hip Hop dance academy needs flyer to promote new kids courses in 2015

We are a dance academy that specializes in breakdancing and hip hop. The product we are offering is a new 10 week breakdancing programme designed for kids aged 8 and up. Purpose of the flyer is to direct people to the website www.groovelantern.com.au so that they can find out more information. Target audience is parents of kids aged 8 - 13. We need the flyer to be eye catching, bold and communicate strength. Add text :
"Do your kids like hip hop music?"
"Do you want your kids to learn good work ethic?"
"Do your kids want to learn awesome dance moves?"
"Check out www.groovelantern.com.au for more information on our 2015 intake"
We would like the design to predominantly use white/black/orange but other colours are fine to support

```html
<!DOCTYPE html>
<html lang="en">
<head>
<meta charset="UTF-8">
<title>Groove Lantern Dance Academy – 2015 Kids Intake Flyer</title>
<link rel="stylesheet" href="https://fonts.googleapis.com/css2?family=Black+Ops+One&family=Allerta+Stencil&family=Exo+2:wght@500;600&display=swap">
<style>
  :root {
    --orange: #f47b2a;
    --white: #ffffff;
    --charcoal: #2b2b2b;
    --ink: #1c1c1c;
    --glow: rgba(255, 255, 255, 0.55);
  }
  html, body {
    margin: 0;
    padding: 0;
    width: 848px;
    height: 1200px;
    overflow: hidden;
    background: var(--charcoal);
  }
  .flyer {
    position: relative;
    width: 848px;
    height: 1200px;
    overflow: hidden;
    background: var(--charcoal);
  }
  .flyer__backdrop {
    position: absolute;
    inset: 0;
  }
  .brand-mark {
    position: absolute;
    left: 585px;
    top: 10px;
    width: 260px;
    height: 260px;
    border-radius: 50%;
    background: var(--white);
    display: flex;
    align-items: center;
    justify-content: center;
    text-align: center;
  }
  .brand-mark__name {
    font-family: "Black Ops One", "Arial Black", sans-serif;
    font-size: 30px;
    line-height: 1.15;
    color: var(--ink);
    letter-spacing: 1px;
  }
  .question {
    position: absolute;
    left: 0;
    width: 848px;
    text-align: center;
  }
  .question__lead {
    display: block;
    font-family: "Black Ops One", "Arial Black", sans-serif;
    font-size: 84px;
    line-height: 1;
    color: var(--orange);
    text-shadow: 0 0 14px var(--glow), 0 0 4px var(--glow);
  }
  .question__body {
    display: block;
    margin-top: 10px;
    font-family: "Allerta Stencil", "Arial", sans-serif;
    font-size: 31px;
    line-height: 1;
    color: var(--white);
    letter-spacing: 1px;
    text-shadow: 0 0 12px var(--glow);
  }
  .question--one { top: 322px; }
  .question--two { top: 520px; }
  .question--three { top: 726px; }
  .call-to-action {
    position: absolute;
    left: 0;
    top: 893px;
    width: 848px;
    text-align: center;
    font-family: "Exo 2", "Arial", sans-serif;
  }
  .call-to-action__intro {
    display: block;
    font-size: 30px;
    font-weight: 600;
    color: var(--orange);
    letter-spacing: 1px;
  }
  .call-to-action__url {
    display: block;
    margin-top: 4px;
    font-size: 54px;
    font-weight: 600;
    color: var(--white);
    letter-spacing: 2px;
    line-height: 1.1;
  }
  .call-to-action__detail {
    display: block;
    margin-top: 4px;
    font-size: 28px;
    font-weight: 600;
    color: var(--orange);
    letter-spacing: 1px;
  }
</style>
</head>
<body>
  <main class="flyer">
    <svg class="flyer__backdrop" width="848" height="1200" viewBox="0 0 848 1200" xmlns="http://www.w3.org/2000/svg">
      <defs>
        <radialGradient id="wall-tone" cx="0.42" cy="0.5" r="0.7">
          <stop offset="0" stop-color="#5a5754"/>
          <stop offset="0.55" stop-color="#3a3938"/>
          <stop offset="1" stop-color="#222222"/>
        </radialGradient>
      </defs>
      <rect class="dancer-photo" x="0" y="0" width="848" height="1200" fill="url(#wall-tone)" role="img" aria-label="Photo of a young breakdancer in a grey cap, white sweatshirt and beige trousers striking a pose against a dark concrete wall"/>
      <path class="wave wave--top-edge" d="M0 0 H848 V20 C700 0 560 0 430 40 C300 80 150 100 0 88 Z" fill="var(--white)"/>
      <path class="wave wave--top" d="M0 0 H848 V12 C700 -6 560 -4 430 32 C300 70 150 90 0 78 Z" fill="var(--orange)"/>
      <path class="wave wave--bottom-edge" d="M0 1108 C170 1085 330 1110 480 1128 C630 1146 760 1110 848 1050 V1200 H0 Z" fill="var(--white)"/>
      <path class="wave wave--bottom" d="M0 1116 C170 1094 330 1118 480 1136 C630 1154 760 1120 848 1060 V1200 H0 Z" fill="var(--orange)"/>
    </svg>

    <div class="brand-mark">
      <span class="brand-mark__name">GROOVE<br>LANTERN<br>DANCE<br>ACADEMY</span>
    </div>

    <section class="question question--one">
      <span class="question__lead">DO YOUR</span>
      <span class="question__body">KIDS LIKE HIP HOP MUSIC?</span>
    </section>
    <section class="question question--two">
      <span class="question__lead">DO YOU</span>
      <span class="question__body">WANT YOUR KIDS TO LEARN GOOD WORK ETHIC?</span>
    </section>
    <section class="question question--three">
      <span class="question__lead">DO YOUR</span>
      <span class="question__body">KIDS WANT TO LEARN AWESOME DANCE MOVES</span>
    </section>

    <section class="call-to-action">
      <span class="call-to-action__intro">Check out</span>
      <span class="call-to-action__url">www.groovelantern.com.au</span>
      <span class="call-to-action__detail">for more information on our 2015 intake</span>
    </section>
  </main>
</body>
</html>
```